vPanel brochure for corporate sector

Our company provides audio visual solutions to the corporate and government markets across Australia. Interactive touch screens are popular in schools and education sectors but are slow to adopt in the corporate market. We wish to create an attention-grabbing A4 single sided colour brochure to promote a state-of-the-art large-format touchscreen product to the financial sector - more specifically for financial planners, board meeting etc. These are available on 55",65",70" and 84" sizes making them ideal for meetings to interact with customers while impressing them with technology.
We have attached a brochure that details the products impressive capability, whcih needs to be summed up in just an A4 brochure.
Key features to include....
-HD resolution of 1920 x 1080
-Screen sizes of 55,65,70 and 84"
-Capture ideas/notes/ direct to internal memory or USB
-Annotate over presentations and save/email/share
-20-point touch (for multiple users at the same time)
-inbuilt Orvix-(brouse the web, access Apps)
-Anti-scratch/Anti-glare screen
-Q-Link wifi for sharing direct from smartphones/tablets
-Multiple inputs for other devices

Special Offer
Fully installed 55” vpanel with wall bracket, USB/VGA/HDMI wall plate and all cabling from only $85.00 inc GST per week for 24 months.(conditions apply)

Design should include company logo, carry across our "BLUE" corporate feel. and contact details (phone, email and web)

Images and previous brochure attached for corporate feel etc.
We feel that some stock images might be required to convey the touchscreen being used in a corporate/professional environment might be required, happy to take your advise on this and purchase if required.

Target Market(s)

Corporate, finance and government

Industry/Entity Type

Government

Font styles to use
Serif
Sans Serif

Colors
3377b5
0255a3

Requirements
Must have
• Be attention-grabbing using the technology and simplicity of the product to gain interest to prospective buyers interested in showing their customers or staff they are an industry leader by adopting technology. Must carry the same KL Orbis corporate feel as previous brochure (attached as sample).
Should not have
• Be cluttered and confusing. Not look like the existing vpanel brochure which is targeted towards education and schools. This product has enormous potential for the business, corporate and government sectors.

```html
<!DOCTYPE html>
<html lang="en">
<head>
<meta charset="utf-8">
<title>KL Orbis Systems – vPanel</title>
<link rel="stylesheet" href="https://fonts.googleapis.com/css2?family=Outfit:wght@300;400;500;700&family=Montserrat:ital,wght@1,800&family=Josefin+Slab:wght@400;600&display=swap">
<style>
  :root {
    --blue-deep: #0d2f8a;
    --blue-mid: #2a6fd0;
    --teal: #1b9ac4;
    --teal-light: #4fb4dc;
    --teal-band: #1a8aa9;
    --charcoal: #3a3a3c;
    --ink: #1c1c1c;
    --white: #ffffff;
  }
  * { margin: 0; padding: 0; box-sizing: border-box; }
  html, body { width: 848px; height: 1200px; overflow: hidden; background: var(--white); }
  .brochure { position: relative; width: 848px; height: 1200px; overflow: hidden; background: linear-gradient(180deg, #f4f8fb 0%, #e6eff5 100%); font-family: "Outfit", sans-serif; font-weight: 300; color: var(--ink); }
  .hero-photo { position: absolute; left: 0; top: 0; width: 848px; height: 640px;
    background: radial-gradient(ellipse at 70% 30%, #6fa6e8 0%, transparent 45%),
                linear-gradient(160deg, #0a2a7a 0%, #1f56b8 45%, #3a7fd8 70%, #2560b8 100%); }
  .shapes { position: absolute; left: 0; top: 0; width: 848px; height: 800px; }
  .brand { position: absolute; left: 34px; top: 564px; display: flex; align-items: center; gap: 12px; font-size: 48px; font-weight: 400; color: var(--ink); letter-spacing: -0.3px; }
  .brand-mark { width: 20px; height: 20px; background: var(--teal); }
  .features-title { position: absolute; left: 268px; top: 638px; font-family: "Montserrat", sans-serif; font-style: italic; font-weight: 800; font-size: 41px; color: var(--teal); text-decoration: underline; text-decoration-thickness: 3px; text-underline-offset: 5px; }
  .feature-list { position: absolute; top: 702px; list-style: none; font-size: 19px; line-height: 24px; letter-spacing: 0.4px; }
  .feature-list li { position: relative; padding-left: 22px; margin-bottom: 8px; text-align: justify; }
  .feature-list li::before { content: ""; position: absolute; left: 2px; top: 7px; width: 0; height: 0; border-left: 5px solid transparent; border-right: 5px solid transparent; border-bottom: 8px solid var(--teal); }
  .feature-list.left { left: 48px; width: 344px; }
  .feature-list.right { left: 452px; width: 346px; }
  .offer-tag { position: absolute; left: 215px; top: 906px; width: 412px; height: 62px; }
  .offer-tag span { position: absolute; inset: 0; display: flex; align-items: center; justify-content: center; font-family: "Josefin Slab", serif; font-weight: 400; font-size: 46px; color: var(--white); letter-spacing: 2px; padding-top: 8px; }
  .offer-band { position: absolute; left: 0; top: 966px; width: 848px; height: 178px; background: var(--teal-band); color: var(--white); text-align: center; }
  .offer-text { margin-top: 8px; font-size: 20px; line-height: 25px; letter-spacing: 0.5px; }
  .offer-rule { width: 300px; height: 1px; background: rgba(255,255,255,0.8); margin: 10px auto 0; position: relative; }
  .offer-rule::after { content: ""; position: absolute; left: 146px; top: -3px; width: 7px; height: 7px; background: var(--white); transform: rotate(45deg); }
  .offer-price { margin-top: 4px; font-size: 23px; }
  .offer-price strong { font-size: 52px; font-weight: 700; letter-spacing: 0; }
  .offer-term { font-size: 23px; line-height: 22px; margin-top: -4px; }
  .offer-conditions { font-size: 15px; margin-left: 200px; }
  .contact-bar { position: absolute; left: 0; top: 1144px; width: 848px; height: 56px; background: var(--charcoal); color: var(--white); display: flex; align-items: center; justify-content: center; gap: 14px; font-size: 18px; letter-spacing: 0.3px; }
</style>
</head>
<body>
<main class="brochure">
  <div class="hero-photo" role="img" aria-label="Stock photo: businesswoman touching floating holographic data screens, with a hand tapping a large touch display"></div>

  <svg class="shapes" viewBox="0 0 848 800" aria-hidden="true">
    <polygon points="0,800 0,510 280,335 575,605 848,470 848,800" fill="#eef4f8"/>
    <polygon points="0,510 280,335 420,465 180,580 0,600" fill="var(--teal-light)" opacity="0.9"/>
    <polygon points="280,335 575,605 520,610 270,400" fill="var(--teal)"/>
    <polygon points="600,480 848,370 848,440 640,520" fill="var(--teal)"/>
    <polygon points="575,612 848,470 848,720" fill="var(--charcoal)"/>
  </svg>

  <div class="brand"><span class="brand-mark"></span>kl orbis systems</div>

  <h2 class="features-title">Key Features:</h2>

  <ul class="feature-list left">
    <li>HD Resolution of 1920 x 1080</li>
    <li>Screen Sizes of 55″ 65″ 70″ and 84″</li>
    <li>Capture Ideas/Notes/ Direct to Internal Memory or USB</li>
    <li>Annotate Over Presentations &amp; Save/Email/Share</li>
    <li>Multiple Inputs for Other Devices</li>
  </ul>
  <ul class="feature-list right">
    <li>20-Point Touch (For Multiple Users at the Same Time)</li>
    <li>Inbuilt Orvix-(Brouse the Web, Access Apps)</li>
    <li>Anti-scratch/Anti-Glare Screen</li>
    <li>Q-Link Wifi for Sharing Direct From Smartphones/Tablets</li>
  </ul>

  <div class="offer-tag">
    <svg width="412" height="62" viewBox="0 0 412 62" aria-hidden="true">
      <polygon points="14,0 398,0 412,31 398,62 14,62 0,31" fill="var(--charcoal)"/>
      <polygon points="20,5 392,5 404,31 392,57 20,57 8,31" fill="none" stroke="var(--white)" stroke-width="2"/>
    </svg>
    <span>Special Offer</span>
  </div>

  <section class="offer-band">
    <p class="offer-text">Fully installed 55″ vpanel with Wall Bracket, USB/VGA/HDMI<br>Wall Plate and All Cabling From.</p>
    <div class="offer-rule"></div>
    <p class="offer-price">Only <strong>$85.00</strong> INC</p>
    <p class="offer-term">GST Per Week for 24 Months.</p>
    <p class="offer-conditions">(Conditions Apply)</p>
  </section>

  <footer class="contact-bar">
    <span>1300 555 019</span><span>|</span><span>www.klorbis.com.au</span><span>|</span><span>Info@klorbis.com.au</span>
  </footer>
</main>
</body>
</html>
```